Kitchen and bathroom exhaust fan cleaning business card design

A new business cleaning domestic - not commercial - exhaust/extractor fans in kitchens, bathrooms and en suites and kitchen range hood filters.

We would like a bright colour suggesting cleanliness (such a syellow or light green?)

I would like to see on the card preferably on the reverse:

"We clean kitchen and bathroom exhaust fans & Volrex Brightos
and
clean and repair range hood filters and replace carbon filters

We give Pensioner discounts
Updates

Designers pls note the TM in the contact filed after Pureflow Vents should be superscript as in the trademark sign. On the reverse of the card, I would like:: "We clean kitchen and bathroom exhaust fans & Volrex Brightos & clean and repair range hood filters and replace carbon filters We give Pensioner discounts

Reason: I will be out of the country for several days

Target Market(s)

people who are too lazy or too busy to clean their fan units and pensioners and others who are unable to do it.

Industry/Entity Type

Business

Contact Information for Business Card

ACT Clean FansTM Designer pls note the TM should be superscript as in the trademark sign
Neil Oakley
Mob: 0431 572 864
Email: pureflowvents@zentromail.com
PO Box 7152, Pellow ACT 2608

Requirements
Must have
• Designer pls note the TM in the contact filed after Pureflow Vents should be superscript as in the trademark sign.

On the reverse

and

```html
<!DOCTYPE html>
<html lang="en">
<head>
<meta charset="utf-8">
<title>Pureflow Vents – Business Card</title>
<link href="https://fonts.googleapis.com/css2?family=Exo+2:wght@300;400;500;600&display=swap" rel="stylesheet">
<style>
  :root {
    --page: #ffffff;
    --frame: #9a9a9a;
    --yellow-deep: #fde10f;
    --yellow-light: #fbf07a;
    --green: #1e8f45;
    --green-text: #2a7d3c;
    --icon-green: #5cc04f;
    --bullet-green: #35b54a;
    --purple: #8b1f83;
    --blade: rgba(215, 190, 20, 0.35);
  }
  * { margin: 0; padding: 0; box-sizing: border-box; }
  html, body { width: 1200px; height: 1000px; overflow: hidden; background: var(--page); }
  body { font-family: "Exo 2", sans-serif; position: relative; }
  .canvas { position: absolute; inset: 0; border: 1px solid var(--frame); }

  .card {
    position: absolute;
    left: 313px;
    width: 572px;
    height: 353px;
    overflow: hidden;
    background: radial-gradient(ellipse at 50% 50%, var(--yellow-light) 0%, var(--yellow-deep) 62%);
  }
  .card--front { top: 93px; }
  .card--back { top: 535px; }

  .blade-glow {
    position: absolute;
    border-radius: 50%;
    background: radial-gradient(circle, var(--blade) 0%, rgba(215,190,20,0) 70%);
  }

  .brand {
    position: absolute;
    color: var(--green);
    font-weight: 600;
    white-space: nowrap;
    letter-spacing: 0.5px;
    word-spacing: 6px;
  }
  .card--front .brand { top: 70px; left: 0; width: 572px; text-align: center; font-size: 50px; }
  .brand sup { font-size: 11px; vertical-align: top; position: relative; top: 8px; margin-left: 3px; letter-spacing: 0; }

  .person { position: absolute; left: 47px; top: 212px; color: var(--green); line-height: 50px; }
  .person__first { font-size: 40px; font-weight: 300; display: block; }
  .person__last { font-size: 40px; font-weight: 500; display: block; }

  .contact { position: absolute; left: 299px; top: 213px; list-style: none; }
  .contact li { display: flex; align-items: center; height: 24px; margin-bottom: 13.5px; font-size: 14px; color: var(--green-text); }
  .contact svg { width: 24px; height: 24px; margin-right: 10px; flex: none; }

  .card--back .brand { top: 30px; right: 57px; font-size: 34px; }
  .services__title { position: absolute; left: 50px; top: 78px; font-size: 23px; font-weight: 500; color: var(--purple); letter-spacing: 1px; word-spacing: 4px; }
  .services { position: absolute; left: 67px; top: 118px; list-style: none; }
  .services li { display: flex; align-items: center; height: 36.5px; font-size: 24px; color: var(--purple); }
  .services li::before { content: ""; width: 14px; height: 14px; border-radius: 50%; background: var(--bullet-green); margin-right: 13px; }
</style>
</head>
<body>
<div class="canvas">

  <section class="card card--front">
    <div class="blade-glow" role="img" aria-label="Faint fan blade decoration" style="left:-40px;top:40px;width:200px;height:200px;"></div>
    <div class="blade-glow" role="img" aria-label="Faint fan blade decoration" style="left:400px;top:140px;width:240px;height:240px;"></div>

    <h1 class="brand">Pureflow Vents<sup>TM</sup></h1>

    <p class="person">
      <span class="person__first">Neil</span>
      <span class="person__last">Oakley</span>
    </p>

    <ul class="contact">
      <li>
        <svg viewBox="0 0 24 24"><circle cx="12" cy="12" r="12" fill="var(--icon-green)"/><path d="M6.5 10.5c0-1.8 2.5-3 5.5-3s5.5 1.2 5.5 3v1h-2.5v-1.2h-6v1.2H6.5z M8 13h8l1 4H7z" fill="#fff"/><circle cx="12" cy="15" r="1.2" fill="var(--icon-green)"/></svg>
        0431 572 864
      </li>
      <li>
        <svg viewBox="0 0 24 24"><circle cx="12" cy="12" r="12" fill="var(--icon-green)"/><rect x="6.5" y="8" width="11" height="8" fill="#fff"/><path d="M6.5 8l5.5 4.5L17.5 8" fill="none" stroke="var(--icon-green)" stroke-width="1"/></svg>
        pureflowvents@zentromail.com
      </li>
      <li>
        <svg viewBox="0 0 24 24"><circle cx="12" cy="12" r="12" fill="var(--icon-green)"/><path d="M12 6l6 5.5h-1.7V17h-3v-3.5h-2.6V17h-3v-5.5H6z" fill="#fff"/></svg>
        PO Box 7152, Pellow ACT 2608
      </li>
    </ul>
  </section>

  <section class="card card--back">
    <div class="blade-glow" role="img" aria-label="Faint fan blade decoration" style="left:-20px;top:-80px;width:200px;height:200px;"></div>
    <div class="blade-glow" role="img" aria-label="Faint fan blade decoration" style="left:390px;top:140px;width:240px;height:240px;"></div>

    <h2 class="brand">Pureflow Vents</h2>
    <h3 class="services__title">WE CLEAN</h3>
    <ul class="services">
      <li>Kitchen and bathroom exhaust fans</li>
      <li>Volrex Brightos</li>
      <li>Clean and repair range hood filters</li>
      <li>Replace carbon filters</li>
      <li>We give Pensioner discounts</li>
    </ul>
  </section>

</div>
</body>
</html>
```